Chicago Train Advertisement for HomeAlongRail.com.

We have purchased one month of advertising on the Chicago NRX subway train. We will have 150 cards up in the subway to advertise our website HomeAlongRail.com where people can search for properties by train station. The cards are 11" tall and 46.5" long. We want people to feel compelled to jump on their cell phones and conduct a search for an apartment or home while they are riding the train, or at least enter their email and search criteria so one of our agents can help them.

Target Market(s)

People who want to live near train stations

Industry/Entity Type

Real Estate

Font styles to use
Sans Serif

Colors

Designer to choose colors to be used in the design.

Requirements
Must have
• The homealongrail logo and a catchy slogan, something like: Find your home near a train station the easy way: www.homealongral.com. Search real estate listings near the NRX or Velco.

```html
<!DOCTYPE html>
<html lang="en">
<head>
<meta charset="utf-8">
<title>HomeAlongRail.com – Train Card</title>
<link rel="stylesheet" href="https://fonts.googleapis.com/css2?family=Nunito+Sans:wght@300;400;600;700&display=swap">
<style>
  :root {
    --night: #0b0a0c;
    --brick: #3a1a12;
    --neon-red: #c8322a;
    --amber: #e08a3a;
    --streak: rgba(220, 235, 255, 0.55);
    --badge-blue: #2aa3dc;
    --white: #ffffff;
  }
  html, body {
    margin: 0;
    padding: 0;
    width: 1200px;
    height: 284px;
    overflow: hidden;
    background: var(--night);
  }
  .train-card {
    position: relative;
    width: 1200px;
    height: 284px;
    overflow: hidden;
    font-family: "Nunito Sans", sans-serif;
    color: var(--white);
  }
  .city-photo {
    position: absolute;
    inset: 0;
    background:
      linear-gradient(168deg, transparent 30%, var(--streak) 34%, transparent 40%),
      linear-gradient(172deg, transparent 62%, rgba(220,235,255,0.35) 66%, transparent 72%),
      radial-gradient(ellipse 120px 150px at 600px 140px, rgba(255,170,80,0.55), transparent 70%),
      radial-gradient(ellipse 420px 260px at 560px 120px, rgba(150,60,30,0.55), transparent 75%),
      linear-gradient(90deg, #2a1a18 0%, var(--brick) 30%, #5a2516 48%, #2b1510 62%, var(--night) 78%, #141216 100%);
  }
  .search-badge {
    position: absolute;
    left: 44px;
    top: 28px;
    width: 168px;
    height: 168px;
    border-radius: 50%;
    background: var(--badge-blue);
    box-shadow: 0 0 0 5px var(--white);
    display: flex;
    align-items: center;
    justify-content: center;
    text-align: center;
    font-weight: 600;
    font-size: 16px;
    line-height: 20px;
  }
  .brand {
    position: absolute;
    right: 24px;
    top: 34px;
    display: flex;
    align-items: center;
    gap: 14px;
  }
  .brand-dot {
    width: 18px;
    height: 18px;
    border-radius: 50%;
    background: var(--white);
  }
  .brand-name {
    font-size: 42px;
    font-weight: 400;
    letter-spacing: -0.5px;
    line-height: 1;
  }
  .tagline {
    position: absolute;
    right: 24px;
    top: 120px;
    margin: 0;
    text-align: right;
    font-size: 14.5px;
    font-weight: 600;
    line-height: 21px;
  }
  .web-address {
    position: absolute;
    right: 24px;
    bottom: 16px;
    font-size: 16px;
    font-weight: 300;
    letter-spacing: 3px;
  }
  .web-address b { font-weight: 700; }
</style>
</head>
<body>
  <main class="train-card">
    <div class="city-photo" role="img" aria-label="Long-exposure night street photo of a downtown theatre with a tall lit marquee sign and red and white light trails from passing traffic"></div>

    <div class="search-badge">
      <span>Search<br>Real Estate<br>Listings<br>near the NRX<br>or Velco</span>
    </div>

    <div class="brand">
      <span class="brand-dot"></span>
      <span class="brand-name">HomeAlongRail.com</span>
    </div>

    <p class="tagline">Find Excellent Housing Opportunities<br>near Train Stations the Easy Way!</p>

    <div class="web-address">www.<b>homealongrail</b>.com</div>
  </main>
</body>
</html>
```